Valtimore Sciences needs high end Label Design for a revolutionary new supplement

We at Valtimore Sciences are looking for a brand new Label Design for a first of its kind product called Tolmisse. It is the first supplement on the market that treats grief and heartbreak. This product is unisex for both men and woman. We want the New Label to look high end and luxurious using the brand colors which are gold and burgundy. Please feel free to use other colors such as black, white, or gray to go along with it or any other colors if you feel would be a great fit! Valtimore Sciences is like the Quorvel of the supplement world, coming out with new products that will challenge the way people treat different symptoms. To Recap:

1. Product Name: TOLMISSE - the font will play a big roll
2. The Label will be placed on an all white bottle
3. Some parts of the label will be printed with foil to make parts of the label shiny and more attractive. Please keep this in mind when designing.
4. Must use our Logo. I will attach a file of our logo and of the emblem as well. Feel free to use the emblem separately if you have a great idea for it. Please let us know if you need the Logo in a different file type.
5. This all natural herbal supplement in pill form is the first to treat grief and support someone with a broken heart. The consumers purchasing this product will be going through a hard and emotional time. This is a serious product.
6. The manufacturer has included some basic instructions regarding the dye line and file types. Please do your best to meet these. If you cannot meet the guidelines please submit art work anyways. If your design is chosen we will just have the manufacturer replicate the design.

The final label should portray Tolmisse and Valtimore Sciences as a luxurious brand and product which was made with cutting edge science leading the way with revolutionary ideas. We want customers to feel that the product is worth every penny, because it is. As soon as they receive the product and take one look at the label, I want them to think WOW I made the right choice buying this. I have attached some Label designs that we really liked for your review.

Please feel free to message me with any questions or if you need the Logo in a different file type. Thank you all.
Updates

Please send in more entries while we take a couple days to review, we are still looking for that one design we can work with. We are getting close, thank you all!

Target Market(s)

People going through grief and heartbreak.

Font styles to use
Sans Serif
Script
Other font styles liked:
• Any font that looks good, The font for the name TOLMISSE is very important and will brand it. We hated the font used in the label we received in our first label draft (attached so you can see)

Requirements
Must have
• Must have the company Logo that says the company name
• Must have the colors Gold and Burgundy
• Must have some areas that will be the shiny foil when label is printed.
• Must say "Dietary Supplement" somewhere near the bottom along with "90 Capsules"
• I have attached a Label someone designed for us but were not really happy with. I did like the font the "Dietary supplement" and "90 Capsules" had and also where it was placed. We absolutely HATED the font used for Tolmisse.
• Must look at the label design we received from the manufacturer and take into consideration the room needed to write in the directions and all the symbols such as "made in america" and "BQH Facility" Don't worry about adding these in as they will put those in before printing but keep in mind they will be added to the Final Label along with the Supplement Facts.
Nice to have
• Would like to see other colors to go with gold and burgundy suck as black, white, or gray. I have attached some Label designs that I really liked for your reference.
Should not have
• Does not need to have any other legal language, that will be applied by the the manufacturer's graphics team.

```html
<!DOCTYPE html>
<html lang="en">
<head>
<meta charset="utf-8">
<title>Tolmisse Dietary Supplement Label</title>
<link rel="stylesheet" href="https://fonts.googleapis.com/css2?family=Raleway:wght@300;400&family=PT+Sans&family=Roboto+Condensed:wght@400;500&display=swap">
<style>
  :root {
    --page: #efdcd4;
    --label-light: #d3c6c2;
    --label-dark: #b9aaa6;
    --gold: #e0a04a;
    --gold-deep: #c9862e;
    --bronze: #b07a4c;
    --band-dark: #7a4323;
    --band-light: #a8632f;
    --chip: #4a2e24;
    --ink: #5a4038;
    --cream: #f7efe6;
  }
  * { margin: 0; padding: 0; box-sizing: border-box; }
  html, body { width: 1200px; height: 1074px; overflow: hidden; }
  body { background: var(--page); position: relative; }
  .label {
    position: absolute; left: 100px; top: 217px; width: 1000px; height: 640px;
    background: linear-gradient(90deg, var(--label-dark), var(--label-light) 40%, var(--label-light) 70%, var(--label-dark));
    overflow: hidden;
  }
  .label-lines { position: absolute; inset: 0; }
  .brand {
    position: absolute; left: 440px; top: 120px; transform: translateX(-50%);
    display: flex; align-items: center; gap: 12px;
    font-family: "Raleway", sans-serif; font-weight: 400; font-size: 22px;
    letter-spacing: 3px; color: var(--bronze); text-transform: uppercase; white-space: nowrap;
  }
  .brand-dot { width: 40px; height: 40px; border-radius: 50%; background: var(--bronze); }
  .product-name {
    position: absolute; left: 440px; top: 300px; transform: translateX(-50%);
    font-family: "Raleway", sans-serif; font-weight: 300; font-size: 118px;
    letter-spacing: 2px; color: var(--gold-deep); line-height: 1; white-space: nowrap;
  }
  .product-type {
    position: absolute; left: 440px; top: 434px; transform: translateX(-50%);
    font-family: "PT Sans", sans-serif; font-size: 38px; letter-spacing: 1.5px;
    color: var(--ink); white-space: nowrap;
  }
  .count {
    position: absolute; left: 380px; top: 540px; height: 62px;
    display: flex; align-items: center; gap: 22px;
    font-family: "Roboto Condensed", sans-serif; font-weight: 500; color: var(--cream);
  }
  .count-number { font-size: 48px; width: 90px; text-align: center; }
  .count-unit { font-size: 36px; letter-spacing: 1.5px; }
  .directions {
    position: absolute; left: 800px; top: 80px; width: 170px;
    font-family: "PT Sans", sans-serif; font-size: 17px; line-height: 1.4; color: var(--ink);
  }
  .directions p + p { margin-top: 22px; }
</style>
</head>
<body>
  <div class="label">
    <svg class="label-lines" width="1000" height="640" viewBox="0 0 1000 640" aria-hidden="true">
      <defs>
        <linearGradient id="band" x1="0" x2="1">
          <stop offset="0" stop-color="var(--band-light)"/>
          <stop offset="1" stop-color="var(--band-dark)"/>
        </linearGradient>
        <linearGradient id="sweep" x1="0" x2="1">
          <stop offset="0" stop-color="var(--gold)"/>
          <stop offset="1" stop-color="var(--gold-deep)"/>
        </linearGradient>
      </defs>
      <path class="gold-sweep" d="M30 0 V500 Q30 560 100 560 H400" fill="none" stroke="url(#sweep)" stroke-width="10"/>
      <rect class="capsule-band" x="300" y="538" width="700" height="62" fill="url(#band)"/>
      <path class="count-chip" d="M385 530 H480 V608 H395 L385 598 Z" fill="var(--chip)"/>
    </svg>

    <div class="brand"><span class="brand-dot"></span>Valtimore Sciences</div>
    <div class="product-name">TOLMISSE</div>
    <div class="product-type">Dietary supplement</div>
    <div class="count"><span class="count-number">90</span><span class="count-unit">CAPSULES</span></div>

    <div class="directions">
      <p>Take two capsules daily with a meal.</p>
      <p>Store in a cool, dry place away from light.</p>
    </div>
  </div>
</body>
</html>
```